Creative UI design for web application

I need a new UI design for my web application. It will be used by small and micro business owners to plan & implement growth tactics.

I've attached the current design (which I'm open to be changed) - but in particular I need to design the centre of the screen, where the work actually happens.

There needs to be place for a title (YOUR BUSINESS) and description (say 1-2 paragraphs of text) - and am happy to include icons or imagery where makes sense. It may make sense for the user to be able to upload their business logo and name, for example.

This screen will be used by the business owner to understand the real value they offer potential customers and their point of difference - why they exist and why potential customers should care.

They'll use the information they put into this screen to plan things like their messaging.

Following that, there needs to be 2 sections in the dashboard.

The first section is titled "WHO YOU ARE"

The first section will include a number of boxes that the user can input information into, as follows:

- Logo
- Business name
- Business tag line
- Business vision
- Business bio
- Brand colours (these should end up as swatches based on the colour code they enter) - the colour code for each colour swatch should also be visible.
- Key competitors
- SWOT analysis (boxes to enter their strengths, weaknesses, opportunities and threats).

The second section is titled "WHY YOU EXIST"

The second section will include a number of boxes that the user can input information (text) into, as follows:

- Who are your ideal customers?
- What problem are you trying to solve for them?
- What pain points will this remove for them?
- How do you solve it?
- How else could this problem be solved?
- Who offers these other solutions?
- Why is your solution better?
- How much does your solution cost?
- What value are you providing to justify this cost?
- How will this make their life/job easier/better?

They should be able to write a decent amount of information in the boxes.

There should ideally be a place for a description for each of these text fields (for both section 1 & 2) as well so I can give them a little bit more direction around what to put in the box. Alternatively there could be a little icon (say a question mark or "i") that they could click on to view instructions. The instructions will be around 2-4 sentences long for each text field.

You have 2 options:

a) This all needs to appear on the one screen, and the navigation needs to be visible (as per the example attached but feel free to recreate this navigation)

Note: the page can scroll below the fold - but please provide the design for the full length of the page.

b) Potentially the 2 sections could actually be in 2 different items in the menu - YOUR BUSINESS and YOUR VALUE (which would sit next to YOUR BUSINESS and before YOUR CUSTOMER in the screenshot provided). feel free to design them as 2 separate screens if you prefer.

I have attached a screenshot of the app as it stands today (screen shot 2017) which would still exist in the new design but under a different section (the learn section from the plan2 mockup attached)

I have mocked up how this new screen could look if broken into 2 and that's also attached. If you can make this come to life - and look more engaging that would be helpful! :)

Target Market(s)

Small and micro business owners

Industry/Entity Type

Marketing

Number of Pages Required

1 page

Font styles to use
Sans Serif
Other font styles liked:
• Montserrat

Colors
87cfc6
d2a4cc
ffffff
85cae6
e8e8e8
5c5c5c

Requirements
Must have
• Use of my brand colours: #cc8eb2, #76d6c8, #68c7ff as well as white and #595959. Must be visually pleasing / engaging, designed for desktop (as it's a desktop application), really easy to use / navigate.
• Use font Montserrat light & Montserrat Regular or Bold. Mostly should be Montserrat light.
Nice to have
• Would be nice to see how this would look on mobile (as the application is responsive) but this is not mandatory.
Should not have
• Should not look too corporate or dry.

```html
<!DOCTYPE html>
<html lang="en">
<head>
<meta charset="utf-8">
<title>Leafstep – Your Business</title>
<link href="https://fonts.googleapis.com/css2?family=Montserrat:wght@300;400;600;700&display=swap" rel="stylesheet">
<style>
:root{
  --teal:#87cfc6;
  --pink:#d2a4cc;
  --blue:#85cae6;
  --page:#e8e8e8;
  --ink:#5c5c5c;
  --dark:#3b3b3b;
  --white:#ffffff;
  --line:#cfcfcf;
}
*{box-sizing:border-box;margin:0;padding:0}
html,body{width:1200px;height:2590px;overflow:hidden}
body{position:relative;background:var(--page);font-family:'Montserrat',sans-serif;font-weight:300;color:var(--ink)}
.abs{position:absolute}

/* top bar */
.topbar{left:0;top:0;width:1200px;height:45px;background:var(--dark)}
.brand{left:135px;top:12px;color:var(--white);font-weight:400;font-size:19px;letter-spacing:1px}
.mainnav a{position:absolute;top:15px;color:#e6e6e6;font-size:12px;font-weight:400;text-decoration:none}
.profile-icon{left:889px;top:11px;width:24px;height:24px;border-radius:50%;background:var(--teal)}
.profile-link{left:922px;top:15px;color:var(--white);font-size:12px;font-weight:400}
.logout{left:1000px;top:10px;width:67px;height:25px;background:var(--pink);color:var(--dark);font-size:12px;font-weight:400;text-align:center;line-height:25px}

/* sub nav */
.subnav{left:0;top:45px;width:1200px;height:41px;background:var(--white);box-shadow:0 6px 10px rgba(0,0,0,.18);z-index:2}
.subnav a{position:absolute;top:0;height:41px;line-height:41px;font-size:12px;font-weight:400;color:var(--ink);text-decoration:none}
.subnav a.active{left:124px;width:113px;text-align:center;background:var(--pink);color:var(--dark)}

/* hero */
.hero{left:0;top:86px;width:1200px;height:470px;background:var(--teal)}
.hero-frame{left:281px;top:202px;width:657px;height:247px;border:2px solid rgba(255,255,255,.45)}
.biz-badge{left:217px;top:134px;width:118px;height:118px;border-radius:50%;background:var(--white);display:flex;align-items:center;justify-content:center;text-align:center;font-size:13px;font-weight:400;color:var(--dark);line-height:1.3}
.biz-name{left:361px;top:129px;font-size:23px;font-weight:400;color:var(--dark)}
.biz-email{left:361px;top:160px;font-size:13px;font-weight:400;color:var(--dark);display:flex;align-items:center;gap:8px}
.hero-copy{left:326px;top:238px;width:590px;font-size:12.5px;line-height:21px;color:var(--dark)}
.hero-copy p+p{margin-top:19px;width:450px}
.hero-photo{left:802px;top:329px;width:188px;height:188px;border-radius:50%;border:4px solid var(--white);background:radial-gradient(circle at 40% 40%,#fbf4f5,#f0dde2 60%,#e3c7cf)}

/* panels */
.panel{background:var(--white);box-shadow:0 18px 16px -10px rgba(0,0,0,.25)}
.panel-head{position:absolute;left:0;top:0;width:100%;height:31px;background:var(--pink);color:var(--white);font-weight:700;font-size:14px;line-height:31px;padding-left:12px;letter-spacing:.3px}
.field{position:absolute;border:1px solid var(--line);background:var(--white)}
.field .label{position:absolute;left:12px;top:11px;font-size:11.5px;font-weight:400;color:var(--dark)}
.info{position:absolute;right:10px;top:9px;width:14px;height:14px}
.field.short .label{top:11px}
.upload{position:absolute;left:187px;top:4px;width:81px;height:26px;background:var(--teal);color:var(--dark);font-size:11px;font-weight:400;display:flex;align-items:center;justify-content:center;gap:6px}
.field.short .info{right:96px}
.field.short.plain .info{right:10px}
.sub-label{position:absolute;font-size:11.5px;font-weight:400;color:var(--dark)}
.swatch{position:absolute;top:943px;width:14px;height:14px}
.save{left:459px;top:2374px;width:282px;height:61px;background:var(--blue);color:var(--white);font-weight:700;font-size:17px;text-align:center;line-height:61px;letter-spacing:.5px}

/* footer */
.footer{left:0;top:2483px;width:1200px;height:107px;background:var(--dark)}
.foot-brand{left:0;width:1200px;top:2505px;text-align:center;color:var(--white);font-weight:400;font-size:18px;letter-spacing:1px}
.copyright{left:0;width:1200px;top:2551px;text-align:center;color:#9a9a9a;font-size:10px}
</style>
</head>
<body>

<header class="abs topbar"></header>
<div class="abs brand">LEAFSTEP</div>
<nav class="abs mainnav" style="left:0;top:0;width:1200px;height:45px">
  <a style="left:352px">Plan</a>
  <a style="left:407px">Learn</a>
  <a style="left:471px">Remember</a>
</nav>
<div class="abs profile-icon"><svg width="24" height="24" viewBox="0 0 24 24"><circle cx="12" cy="9.5" r="3.6" fill="#3b3b3b"/><path d="M5.5 18.5c1.2-3.3 3.8-4.6 6.5-4.6s5.3 1.3 6.5 4.6z" fill="#3b3b3b"/></svg></div>
<div class="abs profile-link">My Profile</div>
<div class="abs logout">Logout</div>

<nav class="abs subnav">
  <a class="active">Your Business</a>
  <a style="left:275px">Your Products</a>
  <a style="left:406px">Your Customers</a>
  <a style="left:558px">Your Goals</a>
  <a style="left:687px">Your Plan</a>
</nav>

<section class="abs hero"></section>
<div class="abs hero-frame"></div>
<div class="abs biz-badge">Mara<br>Quinn</div>
<div class="abs biz-name">Mara Quinn Beauty</div>
<div class="abs biz-email"><svg width="12" height="10" viewBox="0 0 12 10"><rect x=".6" y=".6" width="10.8" height="8.8" fill="none" stroke="#3b3b3b" stroke-width="1.2"/><path d="M.6.8 6 5.4 11.4.8" fill="none" stroke="#3b3b3b" stroke-width="1.2"/></svg>hello@maraquinnbeauty.com</div>
<div class="abs hero-copy">
  <p>There are many variations of passages of Lorem Ipsum available, but the majority have suffered alteration in some form, by injected humour, or randomised words which don't look even slightly believable. If you are going to use a passage of Lorem Ipsum, you need to be sure there isn't anything embarrassing hidden in the middle of text.</p>
  <p>If you are going to use a passage of Lorem Ipsum, you need to be sure there isn't anything embarrassing hidden in the middle of text.</p>
</div>
<div class="abs hero-photo" role="img" aria-label="Flat-lay photo of makeup brushes, lipsticks and palettes on a pale pink surface"></div>

<svg width="0" height="0" style="position:absolute">
  <symbol id="i" viewBox="0 0 14 14"><circle cx="7" cy="7" r="6.3" fill="none" stroke="#8a8a8a" stroke-width="1"/><rect x="6.4" y="5.8" width="1.2" height="4.8" fill="#8a8a8a"/><circle cx="7" cy="3.9" r=".8" fill="#8a8a8a"/></symbol>
</svg>

<!-- Who you are -->
<section class="abs panel" style="left:133px;top:615px;width:934px;height:606px">
  <div class="panel-head">WHO YOU ARE</div>
</section>
<div class="field short" style="left:164px;top:679px;width:275px;height:36px"><span class="label">Logo</span><svg class="info"><use href="#i"/></svg>
  <div class="upload"><svg width="10" height="10" viewBox="0 0 10 10"><path d="M5 0 1.5 3.5h2.2V7h2.6V3.5h2.2z M0.5 8h9v2h-9z" fill="#3b3b3b"/></svg>UPLOAD</div></div>
<div class="field short plain" style="left:461px;top:679px;width:275px;height:36px"><span class="label">Business name</span><svg class="info"><use href="#i"/></svg></div>
<div class="field short plain" style="left:755px;top:679px;width:274px;height:36px"><span class="label">Business tag line</span><svg class="info"><use href="#i"/></svg></div>

<div class="field" style="left:164px;top:737px;width:275px;height:175px"><span class="label">Business vision</span><svg class="info"><use href="#i"/></svg></div>
<div class="field" style="left:461px;top:737px;width:275px;height:175px"><span class="label">Key competitors</span><svg class="info"><use href="#i"/></svg></div>
<div class="field" style="left:755px;top:737px;width:274px;height:175px"><span class="label">Business bio</span><svg class="info"><use href="#i"/></svg></div>

<div class="sub-label" style="left:164px;top:943px;font-weight:300">Brand colours</div>
<span class="swatch" style="left:261px;background:#87cfc6"></span>
<span class="swatch" style="left:281px;background:#d2a4cc"></span>
<span class="swatch" style="left:301px;background:#3bb54a"></span>
<span class="swatch" style="left:321px;background:#3f5fc0"></span>
<span class="swatch" style="left:341px;background:#c23fb0"></span>
<span class="swatch" style="left:361px;background:#f05a24"></span>
<span class="swatch" style="left:381px;background:#5c5c5c"></span>
<span class="swatch" style="left:401px;background:#8a3d1f"></span>
<span class="swatch" style="left:421px;background:#a35cc8"></span>

<div class="sub-label" style="left:167px;top:987px;font-weight:600">SWOT analysis</div>
<div class="field" style="left:164px;top:1012px;width:207px;height:174px"><span class="label">Strengths</span><svg class="info"><use href="#i"/></svg></div>
<div class="field" style="left:382px;top:1012px;width:207px;height:174px"><span class="label">Weaknesses</span><svg class="info"><use href="#i"/></svg></div>
<div class="field" style="left:599px;top:1012px;width:207px;height:174px"><span class="label">Opportunities</span><svg class="info"><use href="#i"/></svg></div>
<div class="field" style="left:818px;top:1012px;width:208px;height:174px"><span class="label">Threats</span><svg class="info"><use href="#i"/></svg></div>

<!-- Why you exist -->
<section class="abs panel" style="left:133px;top:1266px;width:934px;height:1048px">
  <div class="panel-head">WHY YOU EXIST</div>
</section>
<div class="field" style="left:164px;top:1333px;width:421px;height:175px"><span class="label">Who are your ideal customers?</span><svg class="info" style="right:16px"><use href="#i"/></svg></div>
<div class="field" style="left:599px;top:1333px;width:421px;height:175px"><span class="label">What problem are you trying to solve for them?</span><svg class="info" style="right:16px"><use href="#i"/></svg></div>
<div class="field" style="left:164px;top:1525px;width:421px;height:175px"><span class="label">What pain points will this remove for them?</span><svg class="info" style="right:16px"><use href="#i"/></svg></div>
<div class="field" style="left:599px;top:1525px;width:421px;height:175px"><span class="label">How do you solve it?</span><svg class="info" style="right:16px"><use href="#i"/></svg></div>
<div class="field" style="left:164px;top:1714px;width:421px;height:175px"><span class="label">How else could this problem be solved?</span><svg class="info" style="right:16px"><use href="#i"/></svg></div>
<div class="field" style="left:599px;top:1714px;width:421px;height:175px"><span class="label">Who offers these other solutions?</span><svg class="info" style="right:16px"><use href="#i"/></svg></div>
<div class="field" style="left:164px;top:1905px;width:421px;height:175px"><span class="label">Why is your solution better?</span><svg class="info" style="right:16px"><use href="#i"/></svg></div>
<div class="field" style="left:599px;top:1905px;width:421px;height:175px"><span class="label">How much does your solution cost?</span><svg class="info" style="right:16px"><use href="#i"/></svg></div>
<div class="field" style="left:164px;top:2096px;width:421px;height:175px"><span class="label">What value are you providing to justify this cost?</span><svg class="info" style="right:16px"><use href="#i"/></svg></div>
<div class="field" style="left:599px;top:2096px;width:421px;height:175px"><span class="label">How will this make their life/job easier/better?</span><svg class="info" style="right:16px"><use href="#i"/></svg></div>

<div class="abs save">SAVE CHANGES</div>

<footer class="abs footer"></footer>
<div class="abs foot-brand">LEAFSTEP</div>
<div class="abs copyright">Copyrights @ 2017 leafstep.com. All Rights Reserved</div>

</body>
</html>
```